Laminated Training Card; highly professional yet engaging, colorful, fits branding

We need an 8 1/2" x 11" piece, printed front and back, to inspire and offer instructions for nonprofit leaders on key coaching skills to use with their staff. Though it's in a professional services setting, this piece communicates a sense of fun and excitement to encourage leaders to try out these skills, and keep the training card close at hand. An infographic style would be ideal.

Target Market(s)

Nonprofit leaders will use the laminated training card in a face to face training class, and then take it back to the office to use to 'train' their staff

Industry/Entity Type

Training

Font styles to use
Serif

Requirements
Must have
• See project brief attached
Nice to have
Should not have

```html
<!DOCTYPE html>
<html lang="en">
<head>
<meta charset="utf-8">
<title>Coaching Skills Training Card</title>
<link href="https://fonts.googleapis.com/css2?family=Open+Sans:wght@400;600;700&family=Roboto:wght@700;900&display=swap" rel="stylesheet">
<style>
  :root {
    --sky: #abdcef;
    --orange: #e05a2a;
    --brick: #d8502a;
    --slate: #58595b;
    --ink: #1b1b1b;
    --heading-ink: #2b2b2b;
    --white: #ffffff;
    --footer: #121212;
  }
  * { margin: 0; padding: 0; box-sizing: border-box; }
  html, body { width: 848px; height: 1200px; overflow: hidden; background: var(--sky); }
  .card {
    position: relative; width: 848px; height: 1200px; background: var(--sky);
    font-family: "Open Sans", Arial, sans-serif; font-size: 17px; line-height: 23px; color: var(--ink);
  }
  .block { position: absolute; }
  .title-bar {
    position: absolute; left: 28px; top: 40px; width: 506px; height: 54px; background: var(--orange);
  }
  .title-bar h1 {
    position: absolute; left: 274px; top: 13px; font-family: "Roboto", Arial, sans-serif;
    font-weight: 700; font-size: 21px; line-height: 28px; color: var(--ink); letter-spacing: .3px;
  }
  .label-red { color: var(--brick); font-weight: 700; font-size: 15px; }
  .charter {
    position: absolute; left: 28px; top: 399px; width: 820px; height: 224px; background: var(--slate);
  }
  .charter-tab {
    position: absolute; left: 0; top: 0; width: 53px; height: 224px; background: var(--orange);
  }
  .charter-tab span {
    position: absolute; left: 50%; top: 112px; transform: translate(-50%, -50%) rotate(-90deg);
    font-family: "Roboto", Arial, sans-serif; font-weight: 900; font-size: 24px; letter-spacing: .5px;
    color: #2e2e2e; white-space: nowrap;
  }
  .charter p { position: absolute; left: 65px; color: var(--white); }
  .decor { position: absolute; left: 0; top: 0; }
  .section-head {
    position: absolute; font-family: "Roboto", Arial, sans-serif; font-weight: 700; font-size: 23px; line-height: 28px;
  }
  .brag-head { left: 28px; top: 648px; color: var(--brick); font-size: 24px; }
  .mind-head { left: 476px; top: 667px; color: var(--heading-ink); }
  .sources-head { left: 460px; top: 849px; color: var(--heading-ink); }
  .mind-body { left: 476px; top: 712px; color: var(--white); }
  .sources-list { position: absolute; left: 463px; top: 889px; list-style: none; width: 380px; }
  .sources-list li { padding-left: 24px; text-indent: -24px; }
  .sources-list li + li { margin-top: 11px; }
  .footer {
    position: absolute; left: 0; top: 1140px; width: 848px; height: 60px; background: var(--footer);
    color: var(--white); font-size: 17px; line-height: 60px;
  }
  .footer .address { position: absolute; left: 28px; }
  .footer .phone { position: absolute; right: 36px; }
</style>
</head>
<body>
<div class="card">
  <div class="title-bar"><h1>4 TEAM TOXINS</h1></div>

  <p class="block" style="left:28px; top:108px;">Defensiveness, blaming, stonewalling and contempt. We all do it, especially when<br>stress is high. There’s camaraderie through complaining.&nbsp; But left unchecked, great<br>work comes to a halt.</p>
  <p class="block label-red" style="left:28px; top:201px;">ANTIDOTES:</p>
  <p class="block" style="left:28px; top:224px;">Ask: what are you defending? What am I protecting? How can we keep this from<br>spreading?</p>
  <p class="block" style="left:28px; top:294px;">Toxins can flood us. Take a break and come back to the conversation.</p>
  <p class="block" style="left:28px; top:332px;">Check assumptions. I assume you have money in your budget. I assume you don’t<br>want to be&nbsp; in volved. I ssume you’re supporting me on this.’</p>

  <section class="charter">
    <div class="charter-tab"><span>TEAM CHARTER</span></div>
    <p style="top:30px;">Teams don’t find their focus from the mission statement. It’s too broad,<br>vague and doesn’t answer the question: What is our team’s unique<br>SSName your values, what’s your impact, how you celebrate success,<br>even what you do when things go wrong.</p>
    <p style="top:144px;">The Charters answers the questions: if we weren’t SShere, what would be<br>missing? What do we want people to count on from us?</p>
  </section>

  <svg class="decor" width="848" height="1200" viewBox="0 0 848 1200" aria-hidden="true">
    <path d="M620 623 C650 623 668 596 700 594 C732 592 742 612 770 620 C790 626 810 623 848 623 L848 660 L600 660 Z" fill="var(--sky)"/>
    <path d="M463 655 L640 655 C672 655 690 632 726 630 C760 628 790 628 831 628 L831 831 L463 831 Z" fill="var(--orange)"/>
  </svg>

  <h2 class="section-head brag-head">BRAG BITES</h2>
  <p class="block" style="left:28px; top:681px;">Brag on the team. Stay away from<br>generalizations; ‘I have a great team’.<br>Instead name a value you honored, an<br>obstacle overcome, or what others count<br>on. Have 10 team brag bites in your brag<br>bag ready at all times.</p>
  <p class="block" style="left:28px; top:848px;">‘We fell short of the goal. But we never<br>gave up.’</p>
  <p class="block" style="left:28px; top:893px;">We didn’t expect the new people to step<br>up so quickly. We set aside egos and fol-<br>lowed whoever had the best idea.’</p>
  <p class="block" style="left:28px; top:984px;">‘The whole organization counted on our<br>team’s optimism and hopefulness.’</p>

  <h2 class="section-head mind-head">MINDFULNES</h2>
  <p class="block mind-body">Whatever gets your attention gets<br>YOU. Become the director of your<br>attention. Mindfulness strengthens<br>your attention muscles.</p>

  <h2 class="section-head sources-head">SOURCES</h2>
  <ul class="sources-list">
    <li>-&nbsp;&nbsp; How to Speak Up Without Showing Off’ by Rena Holloway</li>
    <li>-&nbsp;&nbsp; Emergence by (need to fill this in)</li>
    <li>-&nbsp;&nbsp; Coaching Practice Institute (CPI): 4-Dimensional Leadership Model</li>
    <li>-&nbsp;&nbsp; Levels of Focus: Martin Aldous &amp; CPI</li>
  </ul>

  <footer class="footer">
    <span class="address">418 Alder Row,&nbsp; Suite 210 Brookfield, OR 97820</span>
    <span class="phone">555-218-0647</span>
  </footer>
</div>
</body>
</html>
```